Shine Barn Auto Care Business Card

2 side business card design for an auto detailing business

Target Market(s)

Auto detailing

Contact Information for Business Card

Things included

The business name “Shine Barn Auto Care”
Owen Marchetti
(403)871-2964
Cedarvale, Sk

Services offered - complete interior& exterior detail
- paint correction & protection
- ceramic coating
- trim restore
- auto carpet & seat cleaning

Requirements
Must have
• Colours that are in my logo

Services offered

My name Owen Marchetti
403-871-2964
Cedarvale, Sk

Not too sure in what order for these ?
Website. Shinebarnautocare.com
Instagram Shinebarnautocare
Email. Shinebarnautoac@mailbox-example.com

```html
<!DOCTYPE html>
<html lang="en">
<head>
<meta charset="utf-8">
<title>Shine Barn Auto Care Business Card</title>
<link rel="stylesheet" href="https://fonts.googleapis.com/css2?family=Montserrat:wght@400;500;700&display=swap">
<style>
  :root {
    --brand-red: #990000;
    --card-white: #ffffff;
    --card-dark: #1f1f1f;
    --ink-dark: #1a1a1a;
    --ink-grey: #555555;
    --stage: #7a7a7a;
  }
  * { margin: 0; padding: 0; box-sizing: border-box; }
  html, body { width: 1200px; height: 1200px; overflow: hidden; }
  body {
    background: var(--stage);
    font-family: "Montserrat", sans-serif;
    position: relative;
  }
  .card {
    position: absolute;
    left: 257px;
    width: 686px;
    height: 392px;
    border-radius: 26px;
    overflow: hidden;
  }
  .card--front { top: 165px; background: var(--card-white); }
  .card--back { top: 653px; background: var(--card-dark); }

  /* front: brand block */
  .brand {
    position: absolute;
    left: 140px;
    top: 110px;
    width: 168px;
    text-align: center;
  }
  .brand__dot {
    display: block;
    width: 62px;
    height: 62px;
    margin: 0 auto 10px;
    border: 5px solid var(--brand-red);
    border-radius: 50%;
  }
  .brand__name {
    font-weight: 500;
    font-size: 19px;
    line-height: 1.15;
    letter-spacing: 1px;
    color: var(--ink-dark);
    text-transform: uppercase;
  }
  .divider {
    position: absolute;
    left: 330px;
    top: 113px;
    width: 1px;
    height: 116px;
    background: var(--ink-dark);
  }
  .contact {
    position: absolute;
    left: 353px;
    top: 106px;
  }
  .contact__name {
    font-weight: 500;
    font-size: 24px;
    letter-spacing: 0.5px;
    color: var(--brand-red);
    text-transform: uppercase;
  }
  .contact__city {
    margin-top: 8px;
    font-size: 15.5px;
    color: var(--ink-grey);
    letter-spacing: 0.4px;
  }
  .contact__list { list-style: none; margin-top: 12px; }
  .contact__item {
    display: flex;
    align-items: center;
    gap: 9px;
    font-size: 16px;
    line-height: 19.5px;
    color: var(--ink-grey);
    letter-spacing: 0.3px;
  }
  .contact__icon { width: 13px; height: 13px; fill: var(--brand-red); flex: none; }

  .services-band {
    position: absolute;
    left: 0;
    top: 286px;
    width: 100%;
    height: 75px;
    background: var(--brand-red);
    color: var(--card-white);
    text-align: center;
    padding-top: 8px;
  }
  .services__title { font-weight: 700; font-size: 16.5px; line-height: 19px; }
  .services__line { font-size: 16px; line-height: 20px; letter-spacing: 0.5px; }
  .sep { display: inline-block; width: 7px; height: 7px; border-radius: 50%; background: currentColor; margin: 0 7px; vertical-align: middle; }

  /* back */
  .back-mark {
    position: absolute;
    left: 268px;
    top: 92px;
    width: 150px;
    height: 150px;
    border: 12px solid var(--brand-red);
    border-radius: 50%;
    display: flex;
    align-items: center;
    justify-content: center;
    text-align: center;
  }
  .back-mark__name {
    font-weight: 700;
    font-size: 15px;
    line-height: 1.2;
    color: var(--brand-red);
    text-transform: uppercase;
  }
  .back-services {
    position: absolute;
    left: 0;
    top: 274px;
    width: 100%;
    text-align: center;
    color: var(--card-white);
  }
  .back-services__title {
    font-weight: 700;
    font-size: 16.5px;
    color: var(--brand-red);
    text-transform: uppercase;
    margin-bottom: 8px;
  }
  .back-services .sep { background: var(--brand-red); }
</style>
</head>
<body>
  <section class="card card--front">
    <div class="brand">
      <span class="brand__dot"></span>
      <p class="brand__name">Shine Barn<br>Auto Care</p>
    </div>
    <div class="divider"></div>
    <div class="contact">
      <h1 class="contact__name">Owen Marchetti</h1>
      <p class="contact__city">Cedarvale, Sk</p>
      <ul class="contact__list">
        <li class="contact__item">
          <svg class="contact__icon" viewBox="0 0 24 24"><path d="M6.6 10.8a15.1 15.1 0 0 0 6.6 6.6l2.2-2.2a1 1 0 0 1 1-.25 11.4 11.4 0 0 0 3.6.57 1 1 0 0 1 1 1V20a1 1 0 0 1-1 1A17 17 0 0 1 3 4a1 1 0 0 1 1-1h3.5a1 1 0 0 1 1 1c0 1.25.2 2.45.57 3.57a1 1 0 0 1-.25 1z"/></svg>
          (403)871-2964
        </li>
        <li class="contact__item">
          <svg class="contact__icon" viewBox="0 0 24 24"><path d="M2 5h20v14H2z M2 5l10 7 10-7" fill="var(--brand-red)" stroke="#fff" stroke-width="1.6"/></svg>
          info@shinebarn.com
        </li>
        <li class="contact__item">
          <svg class="contact__icon" viewBox="0 0 24 24"><circle cx="12" cy="12" r="10"/><path d="M7 7c3 0 3 3 5 3s1 4-1 5-1 4-1 4M15 5c0 2 2 3 4 3" fill="none" stroke="#fff" stroke-width="1.6"/></svg>
          www.shinebarn.com
        </li>
      </ul>
    </div>
    <div class="services-band">
      <p class="services__title">complete interior &amp; exterior detail</p>
      <p class="services__line">Paint correction &amp; Protection<span class="sep"></span>Ceramic coating</p>
      <p class="services__line">Trim restore<span class="sep"></span>Auto carpet &amp; Seat cleaning</p>
    </div>
  </section>

  <section class="card card--back">
    <div class="back-mark">
      <p class="back-mark__name">Shine Barn<br>Auto Care</p>
    </div>
    <div class="back-services">
      <p class="back-services__title">Complete interior &amp; exterior detail</p>
      <p class="services__line">Paint correction &amp; Protection<span class="sep"></span>Ceramic coating</p>
      <p class="services__line">Trim restore<span class="sep"></span>Auto carpet &amp; Seat cleaning</p>
    </div>
  </section>
</body>
</html>
```